Website for music record label
Thistle Quarry
Project: Website for music record label
Website for music record label - Music
Creative Brief
Music
www.thistlequarry-example.com
We are a small record label that helps bands record, engineer, distribute, and promote their music.
top
http://www.ferngroovetunes-example.com/index_2.html
http://www.pebble-sound-example.com/
http://vinylhousediscs-example.org/
Was thinking about making the top navigation section to look like an "Amp Head": (example below) 1) Bramble, https://www.brambleamps-example.com/ 2) Pemberton, http://www.pembertonamps-example.com/products/amps/ 3) Volt 9, http://volt9-example.com/amps/ Ref http://www.ferngroovetunes-example.com/index_2.html The buttons & switches can change the website pages... Also want our LOGO on the "Amp Head" (hyperlinked back to the home page. Menus: Home, News, Bands, Store, Contact Us Might make the "MAIN" area of the website be framed inside the "Amp Cabinet" (area where the speakers are) but its up to yall... whatever looks cool
thistlequarry thistlequarry
Also, Pell... in the content area.... you have our logo black and its hard to read.. can you make it white or light gray on that? thanks
omg, i just wrote tons but clicked on a draft and it all got erased.. LOL jahs djlkah sdjasd ok, thanks again for the all work, we are almost done.. here are the final tweaks: 1) i like the backgrounds on draft #34 & #35... the dark greens are looking good! 2) the top handle needs to be lower profile if possible (pell - yours is too high) and trim the extra space above the handle to get the amp head up as high as possible. 3) the feet at the bottom of the lower amp cabinet need to look more real if possible (shinecraft - yours need work) :) 4) if the buttons, knobs, look as if they turn or are pushed or light up when selected. 5) remove music player from amp plate to add it to the amp head edge molding under the handle. i can purchase a music player if needed... ref link: http://widgetbarn-example.net/item/night-comet-mp3-player-pro/16660?ref=tuts2 http://widgetbarn-example.net/item/thin-frame-xml-mp3-player/21045 6) kinda want to keep the amp head (nav area as small as possible height wise) so pell you might want to delete the music playing area off you latest drafts and shorten the height - and shinecraft, yours looks fine 7) also, the amp cloth material (like where the logo is and the lower content section) needs to be a little darker black (especially Pells / shinecraft is fine) Other than that guys, they look great and cant wait to see the finals :)
Why did "pelldrafter" withdraw ALL of their concepts?
all right, we are getting close to the end. all of them are looking great and its going to be a tough choice. great job all.
OK, new info has came to light. I showed my business partner the designs.... He (we) agreed that we like the dual stack setup (like in draft#4) the amp head sitting on the amp cabinet. Basically the upper and lower configuration. Also, we are going with the GOLD plate and keep the white outlines around the amp and cabinet. Plus we like the background used on #2 & #21 but might try 1 layout using the greenish color on out logo instead of the gray. Also, there is a gap between the upper & lower amp sections... please remove this and make it appear they are sitting on top of each other. Thanks ALL!
Feedback for keystone - Overall, all of yours look cool. Nice and clean. Not much to dislike on, just review the comments for the other guys and see if any of that helps you. might integrate friendbook, chirper, etc into the mix and also a music player. Very nice job so far.
Feedback for Pelldrafter draft#10: overall the 1 piece amp looks killer! totally digging how you integrated the music player into the upper panel, awesome. I would put a button over each knob to light up when you are on that page. The handle on the top is a bit too big. Dont like the black logo at the bottom of the page. looks weird. Other than that, awesome job.
here is feedback that i gave "shinecraft" ok shinecraft. what you are doing is killer! AWESOME JOB. Here are some suggestions for "shinecraft" - love the background on #2 & #21. Personally, i like the 1 piece amp/head combo like #21 and I like the GREEN button plate, BUT my friends like the GOLD button plate and the 2 piece head/amp cabinet like #2. so im confused :( I think the 2 piece cabinet loses too much room and people will have to scroll more, but it looks badass. About the handle on the top... i could take it or leave it.. either way im not crushed, but it does look cooler with it but we should trim the extra at the top until to almost touches the handle if we leave it. And might rearrange the button area to added the friendbook, chirper, etc buttons on the control head. and please remove the angled logo on the button panel. Thanks. Actually I still think i like the 1 piece cabinet draft#21 just because its more compact. Please reference Volt 9 / Falcon Range amp heads... http://volt9-example.com/amps/#falcon maybe you can incorporate the Thistle Quarry logo into the control head the same way like were he comes down and has the logo. Also, i want to incorporate a "music player" into the design. It can be on the control panel (button plate) or on the top panel of the amp head (like under the handle) Oh and on the knobs and buttons you created... the number should be 0, 2, 4, 6, etc,... i think you have 0, 6, 4, 6, etc... and whichever color scheme we settle on GOLD or GREEN, can you make a line around the whole amp inside from white to that color. Thanks shinecraft

```html
<!DOCTYPE html>
<html lang="en">
<head>
<meta charset="utf-8">
<title>Thistle Quarry — Record Label</title>
<link rel="stylesheet" href="https://fonts.googleapis.com/css2?family=Bree+Serif&family=Roboto:wght@400;500;700&family=Great+Vibes&family=Droid+Serif&display=swap">
<style>
:root{
  --bg-deep:#0c1a08;
  --bg-mid:#274a1c;
  --tolex:#2b2b2b;
  --tolex-light:#4a4a4a;
  --cloth:#1d1d1d;
  --cloth-dark:#161616;
  --gold:#e9b262;
  --gold-dark:#d39a48;
  --green:#1b9a3a;
  --green-bright:#2bbf4b;
  --text:#e4e4e4;
  --muted:#bdbdbd;
  --rule:#3a3a3a;
  --white-line:#f2f2f2;
}
*{box-sizing:border-box;margin:0;padding:0}
html,body{width:874px;height:1200px;overflow:hidden}
body{
  background:radial-gradient(ellipse at 50% 20%,var(--bg-mid),var(--bg-deep) 80%);
  font-family:'Roboto',sans-serif;color:var(--text);position:relative;
}
.abs{position:absolute}
/* amp shells */
.shell{position:absolute;left:99px;width:676px;border-radius:20px;
  background:linear-gradient(180deg,var(--tolex-light),var(--tolex) 12%,#242424 88%,#3b3b3b);
  box-shadow:0 6px 16px rgba(0,0,0,.7), inset 0 0 0 2px #1a1a1a}
.screw{position:absolute;width:7px;height:7px;border-radius:50%;background:radial-gradient(#ddd,#777);}
.panel{position:absolute;left:140px;width:592px;border:3px solid var(--white-line);border-radius:3px;overflow:hidden}
.handle{position:absolute;left:365px;top:6px;width:147px;height:16px;border:5px solid #3a3a3a;border-bottom:none;border-radius:10px 10px 0 0}
.foot{position:absolute;top:1172px;width:42px;height:20px;background:linear-gradient(#333,#111);border-radius:0 0 8px 8px}
/* player */
.player{position:absolute;left:309px;top:29px;width:250px;height:28px;background:#111;border:2px solid #444;border-radius:2px;font-size:5px;color:#d6e84a;letter-spacing:.3px}
.player .track{position:absolute;left:50px;top:3px;width:140px;height:9px;background:#050505;border:1px solid #333;padding:1px 3px;line-height:6px}
.player .time{position:absolute;left:6px;top:16px;line-height:6px}
.player .bar{position:absolute;top:18px;height:3px;border-radius:2px}
.player .ctl{position:absolute;left:6px;top:4px;color:#777;font-size:6px}
.player .shuf{position:absolute;right:6px;top:16px;color:#888}
/* head */
.head-cloth{height:103px;background:repeating-linear-gradient(45deg,var(--cloth) 0 2px,var(--cloth-dark) 2px 4px)}
.brand{position:absolute;left:0;right:0;top:30px;text-align:center;font-family:'Bree Serif',serif;font-size:40px;color:#fff;letter-spacing:3px}
.brand .dot{display:inline-block;width:30px;height:30px;border-radius:50%;background:var(--green);vertical-align:-3px;margin:0 12px}
.plate{height:66px;background:linear-gradient(var(--gold),var(--gold-dark));position:relative}
.power{position:absolute;left:13px;top:3px;width:34px;height:46px;background:#111;border:2px solid #555;border-radius:2px}
.power::after{content:"";position:absolute;left:6px;top:5px;width:18px;height:28px;background:linear-gradient(#444,#1c1c1c);border-radius:2px}
.power-label{position:absolute;left:13px;top:52px;font-size:8px;font-weight:700;color:#222}
.social-dot{position:absolute;left:73px;width:22px;height:22px;border-radius:50%;background:#222}
.nav{position:absolute;top:0;list-style:none}
.nav li{position:absolute;width:60px;text-align:center;top:9px}
.knob{width:37px;height:37px;margin:0 auto;border-radius:50%;
  background:radial-gradient(circle at 40% 35%,#f5f5f5,#9a9a9a 55%,#3b3b3b);box-shadow:0 2px 3px rgba(0,0,0,.5);position:relative}
.knob::after{content:"";position:absolute;left:50%;top:6px;width:2px;height:11px;background:#222;transform:translateX(-50%) rotate(-30deg);transform-origin:50% 100%}
.knob.active{box-shadow:0 0 0 3px var(--green-bright),0 2px 4px rgba(0,0,0,.5)}
.nav a{display:block;margin-top:6px;font-size:11px;font-weight:500;color:#222;text-decoration:none}
.nav .on a{color:var(--green)}
/* cabinet */
.cloth{background:repeating-linear-gradient(45deg,var(--cloth) 0 2px,var(--cloth-dark) 2px 4px)}
.hero-photo{position:absolute;left:0;top:0;width:391px;height:201px;background:linear-gradient(120deg,#6d5a47,#2e261f 60%,#8a7763)}
.hero-copy{position:absolute;left:391px;top:0;width:195px;height:201px;background:linear-gradient(var(--green),#14802f);padding:10px 10px}
.hero-copy h2{font-family:'Great Vibes',cursive;font-weight:400;font-size:22px;line-height:20px;color:#fff}
.hero-copy p{font-family:'Droid Serif',serif;font-size:8.4px;line-height:12.4px;margin-top:11px;color:#f1f1f1}
.btn-read{display:inline-block;margin-top:11px;background:#c8874b;color:#222;font-family:'Droid Serif',serif;font-size:8.5px;padding:3px 7px;border-radius:2px}
.dots{position:absolute;right:2px;bottom:6px}
.dots span{display:inline-block;width:9px;height:9px;border-radius:50%;background:#0c5e20;margin-left:3px}
.dots span:first-child{background:var(--green-bright)}
.welcome{position:absolute;left:11px;top:237px;font-family:'Bree Serif',serif;font-size:21px;color:#fff}
.welcome .mark{display:inline-block;width:22px;height:22px;border-radius:50%;background:var(--green);vertical-align:-3px;margin-right:8px}
.welcome em{font-style:normal;color:var(--green-bright)}
.intro{position:absolute;left:11px;top:265px;width:566px;font-size:9.6px;line-height:15.2px;letter-spacing:.15px;color:var(--text)}
.sec-title{position:absolute;font-size:15px;font-weight:500;color:#fff;display:flex;align-items:center;gap:6px}
.sec-title em{font-style:normal;color:var(--green-bright)}
.rule{position:absolute;height:1px;background:var(--rule)}
.dash{position:absolute;height:0;border-top:1px dashed #555}
.item h3{font-size:10.3px;font-weight:700;color:#fff}
.item p{font-size:9.4px;line-height:13.5px;color:var(--muted);margin-top:3px}
.thumb{position:absolute;border:2px solid #ddd}
.date{position:absolute;width:33px;height:34px;background:var(--green);border-radius:2px;text-align:center;color:#fff;line-height:1}
.date b{display:block;font-weight:400;font-size:14px;padding-top:3px;background:#0d4d1c;height:17px}
.date span{font-size:9px}
.more{position:absolute;font-size:8.6px;color:#ddd}
.arrows span{display:inline-block;width:12px;height:12px;border-radius:50%;border:1.5px solid #ccc;margin-left:3px}
.share{display:flex;align-items:center;gap:6px;font-size:8.6px;font-weight:700;margin-top:8px;color:#ddd}
.share i{display:inline-block;width:13px;height:13px;background:#ddd;border-radius:1px}
.footer h4{position:absolute;font-size:12px;font-weight:500;color:#fff}
.footer h4 em{font-style:normal;color:var(--green-bright)}
.footer .small{position:absolute;font-size:7.8px;color:#aaa;line-height:10px}
.email-field{position:absolute;width:157px;height:20px;border:1px solid #555;background:#1c1c1c;font-size:7.5px;font-style:italic;color:#777;padding:5px 6px}
.subscribe{position:absolute;background:var(--green);color:#fff;font-size:9px;font-weight:700;padding:3px 6px;border-radius:1px}
.contact-row{position:absolute;display:flex;gap:9px;font-size:8.2px;color:#ddd;line-height:9.5px}
.vrule{position:absolute;width:1px;background:#2c2c2c}
.sq{position:absolute;width:21px;height:21px;border-radius:2px}
</style>
</head>
<body>

<!-- amp head -->
<div class="handle"></div>
<div class="shell" style="top:20px;height:236px">
  <span class="screw" style="left:15px;top:14px"></span><span class="screw" style="right:15px;top:14px"></span>
  <span class="screw" style="left:24px;bottom:24px"></span><span class="screw" style="right:24px;bottom:24px"></span>
</div>
<div class="player" aria-label="Music player">
  <span class="ctl">◀◀ ❚❚ ▶▶</span>
  <div class="track">01. RUST ORCHARD - KELP STUDIOS</div>
  <span class="time">00:13 / 01:25</span>
  <span class="bar" style="left:58px;width:72px;background:#e38a1c"></span>
  <span class="bar" style="left:148px;width:60px;background:#39c23a"></span>
  <span class="shuf">SHUFFLE</span>
</div>
<div class="panel" style="top:63px;height:173px">
  <div class="head-cloth">
    <a class="brand">THISTLE<span class="dot"></span>QUARRY</a>
  </div>
  <div class="plate">
    <div class="power"></div>
    <span class="power-label">POWER</span>
    <span class="social-dot" style="top:6px" aria-label="friendbook"></span>
    <span class="social-dot" style="top:35px" aria-label="chirper"></span>
    <ul class="nav">
      <li class="on" style="left:262px"><div class="knob active"></div><a>HOME</a></li>
      <li style="left:325px"><div class="knob"></div><a>NEWS</a></li>
      <li style="left:388px"><div class="knob"></div><a>BANDS</a></li>
      <li style="left:450px"><div class="knob"></div><a>STORE</a></li>
      <li style="left:513px"><div class="knob"></div><a>CONTACT</a></li>
    </ul>
  </div>
</div>

<!-- cabinet -->
<div class="shell" style="top:256px;height:919px">
  <span class="screw" style="left:15px;top:14px"></span><span class="screw" style="right:15px;top:14px"></span>
  <span class="screw" style="left:24px;bottom:18px"></span><span class="screw" style="right:24px;bottom:18px"></span>
</div>
<div class="foot" style="left:167px"></div><div class="foot" style="left:666px"></div>

<div class="panel cloth" style="top:297px;height:859px">
  <div class="hero-photo" role="img" aria-label="Sepia photo of hands working a DJ mixing deck"></div>
  <div class="hero-copy">
    <h2>Duis autem vel eum iriure dolor inhendrerit</h2>
    <p>Lorem ipsum dolor sitamet,consectetuer adipiscing elit, sed diam nonummy nibh euismod tincidunt ut laoreet dolore magna aliquam erat volutpat. Ut wisi enim ad minim veniam.</p>
    <span class="btn-read">Read More</span>
    <div class="dots"><span></span><span></span><span></span><span></span></div>
  </div>

  <h1 class="welcome"><span class="mark"></span>Welcome to <em>Thistle Quarry</em></h1>
  <p class="intro">Conveniently located in Fullerton and Studio City, Brightpath Paving is an award-winning, family owned paving contractor specializing in the design and installation of high quality paving stones for commercial and residential properties throughout Southern California. We are completely customer focused and believe the quality of our work extends through the way we manage projects and serve our customers.</p>

  <!-- new releases -->
  <h2 class="sec-title" style="left:11px;top:343px">
    <svg width="24" height="24" viewBox="0 0 24 24"><polygon points="12,1 15,9 23,9 17,14 19,22 12,17 5,22 7,14 1,9 9,9" fill="none" stroke="#2bbf4b" stroke-width="2"/></svg>
    NEW <em>RELEASES</em></h2>
  <div class="rule" style="left:11px;top:372px;width:265px"></div>
  <div class="thumb" style="left:11px;top:383px;width:55px;height:41px;background:linear-gradient(135deg,#b8331c,#3a0d07)" role="img" aria-label="Concert crowd photo"></div>
  <div class="item abs" style="left:78px;top:380px;width:210px"><h3>Maecenas consequat solldinc tempdusr</h3><p>Donec fermentum in leo nec biben Curabitur tincidunt orci nec lorem pulvina ut porta mi.</p></div>
  <div class="dash" style="left:11px;top:433px;width:265px"></div>
  <div class="thumb" style="left:11px;top:441px;width:55px;height:41px;background:linear-gradient(135deg,#7a1d18,#2a2f3a)" role="img" aria-label="Guitarist close-up photo"></div>
  <div class="item abs" style="left:78px;top:438px;width:210px"><h3>Biben conequat solldinc tempdusr</h3><p>Donec fermentum in leo nec biben Curabitur tincidunt orci nec lorem pulvina ut porta mi.</p></div>
  <span class="more" style="left:229px;top:494px">Read More »</span>

  <!-- latest news -->
  <h2 class="sec-title" style="left:317px;top:343px">
    <svg width="22" height="20" viewBox="0 0 22 20"><path d="M2 7h5l10-5v16L7 13H2z" fill="#fff"/><rect x="4" y="13" width="3" height="6" fill="#2bbf4b"/></svg>
    LATEST <em>NEWS</em></h2>
  <div class="rule" style="left:307px;top:372px;width:270px"></div>
  <div class="date" style="left:317px;top:386px"><b>12</b><span>Feb</span></div>
  <div class="item abs" style="left:363px;top:383px;width:215px"><p>Maecenas consequat sollicitudin quam ac tepus. Donec fermentum in leo nec bibendum. Curabitur tincidunt orci nec lorem pulvinar, ut porta mi.</p></div>
  <div class="dash" style="left:307px;top:433px;width:270px"></div>
  <div class="date" style="left:317px;top:448px"><b>16</b><span>Feb</span></div>
  <div class="item abs" style="left:363px;top:445px;width:215px"><p>Maecenas consequat sollicitudin quam ac tepus. Donec fermentum in leo nec bibendum. Curabitur tincidunt orci nec lorem pulvinar, ut porta mi.</p></div>
  <span class="more" style="left:525px;top:494px">Read More »</span>

  <!-- downloads -->
  <h2 class="sec-title" style="left:11px;top:541px">
    <svg width="22" height="20" viewBox="0 0 22 20"><path d="M8 0h6v7h5l-8 8-8-8h5z" fill="#2bbf4b"/><path d="M1 14v5h20v-5" fill="none" stroke="#fff" stroke-width="2"/></svg>
    DOWNLOADS</h2>
  <div class="arrows abs" style="right:10px;top:549px"><span></span><span></span></div>
  <div class="rule" style="left:11px;top:570px;width:566px"></div>
  <div class="thumb" style="left:11px;top:580px;width:133px;height:89px;border:3px solid #555;background:linear-gradient(160deg,#2c1e16,#a04e22 55%,#1d1713)" role="img" aria-label="Photo of a guitarist performing on stage"></div>
  <div class="item abs" style="left:154px;top:578px;width:135px"><h3>Fusce Rhoncus Retmania</h3><p style="font-size:8.6px;line-height:11.6px">Maecenas conseqat sollicitudin quam ac tepus. Donec fermumt in leo nec bibendum. Curabiturr tincidunt orci nec lorem</p>
    <div class="share">Share with: <i></i><i></i><i></i><i></i></div></div>
  <div class="thumb" style="left:302px;top:580px;width:133px;height:89px;border:3px solid #555;background:linear-gradient(160deg,#0d1a45,#2f5fc9 50%,#0a0f22)" role="img" aria-label="Photo of a band playing under blue stage lights"></div>
  <div class="item abs" style="left:445px;top:578px;width:135px"><h3>Maecenason Gyafania</h3><p style="font-size:8.6px;line-height:11.6px">Maecenas conseqat sollicitudin quam ac tepus. Donec fermumt in leo nec bibendum. Curabiturr tincidunt orci nec lorem</p>
    <div class="share">Share with: <i></i><i></i><i></i><i></i></div></div>

  <!-- footer -->
  <div class="footer">
    <div class="rule" style="left:0;top:701px;width:586px;background:#111;height:2px"></div>
    <h4 style="left:14px;top:728px">SIGN UP <em>NEWSLETTER</em></h4>
    <div class="rule" style="left:14px;top:748px;width:150px"></div>
    <p class="small" style="left:14px;top:756px;width:150px">Signup with us and get update in your inbox.</p>
    <div class="email-field" style="left:13px;top:782px">Enter your Email...</div>
    <span class="subscribe" style="left:14px;top:811px">Subscribe</span>
    <div class="vrule" style="left:197px;top:730px;height:115px"></div>

    <h4 style="left:231px;top:728px">CONTACT <em>US</em></h4>
    <div class="rule" style="left:231px;top:748px;width:105px"></div>
    <div class="contact-row" style="left:233px;top:757px">
      <svg width="9" height="13" viewBox="0 0 9 13"><path d="M4.5 0A4.5 4.5 0 0 0 0 4.5C0 8 4.5 13 4.5 13S9 8 9 4.5A4.5 4.5 0 0 0 4.5 0z" fill="#ccc"/><circle cx="4.5" cy="4.5" r="1.6" fill="#1d1d1d"/></svg>
      <span>Lorem ipsum dolor sit<br>conse adipisicing<br>elitsed</span></div>
    <div class="contact-row" style="left:233px;top:800px">
      <svg width="8" height="11" viewBox="0 0 8 11"><rect x="0.5" y="0.5" width="7" height="10" rx="1" fill="none" stroke="#ccc"/><rect x="2" y="2" width="4" height="4" fill="#ccc"/></svg>
      <span>1-555-014-2287</span></div>
    <div class="contact-row" style="left:233px;top:821px">
      <svg width="11" height="8" viewBox="0 0 11 8"><rect x="0.5" y="0.5" width="10" height="7" fill="none" stroke="#ccc"/><path d="M0.5 0.5l5 4 5-4" fill="none" stroke="#ccc"/></svg>
      <span>info@thistlequarry.com</span></div>
    <div class="vrule" style="left:370px;top:730px;height:115px"></div>

    <h4 style="left:406px;top:728px">SOCIALIZE <em>WITH US</em></h4>
    <div class="rule" style="left:406px;top:748px;width:175px"></div>
    <span class="sq" style="left:445px;top:768px;background:#3b5aa3" aria-label="friendbook"></span>
    <span class="sq" style="left:476px;top:768px;background:#2aa6e0" aria-label="chirper"></span>
    <p class="small" style="left:406px;top:800px;width:175px;text-align:center;color:#ddd;font-size:8.2px;line-height:12px">Copyright © 2014 Thistle Quarry<br>All Rights Reserved.</p>
  </div>
</div>

</body>
</html>
```